Property risk and finance brokerage company needs a business card design

Tarlow Financial requires a business card design. Please integrate existing logo (refer uploaded file).
hex codes used on logo #002649 #008ED6 #444F51 #ADAFAA
font used - Cinzel
Contact information
Renata Sollisford
Director
Mobile: 0491 738 205
email: r.sollisford@tarlowfinancial.example.au
website: www.tarlowfinancial.example.au
CRN : 918354
PO Box 527
Larkfield, Victoria, 3188
Horizontal orientation please
Finance

```html
<!DOCTYPE html>
<html lang="en">
<head>
<meta charset="utf-8">
<title>Tarlow Financial — Business Card</title>
<link rel="stylesheet" href="https://fonts.googleapis.com/css2?family=Cinzel:wght@400;500&family=Gentium+Book+Plus&display=swap">
<style>
  :root{
    --navy:#002649;
    --blue:#008ED6;
    --slate:#444F51;
    --stone:#ADAFAA;
    --paper:#f4f4f3;
    --ground:#dcdcda;
  }
  *{box-sizing:border-box;margin:0;padding:0}
  html,body{width:1200px;height:900px;overflow:hidden}
  body{
    background:var(--ground);
    font-family:"Gentium Book Plus",Georgia,serif;
    color:var(--slate);
    position:relative;
  }
  .card{
    position:absolute;
    left:290px;
    width:620px;
    height:354px;
    background:var(--paper);
    box-shadow:0 6px 18px rgba(0,0,0,.18);
  }
  .card--front{top:60px}
  .card--back{top:486px}

  .wordmark{display:flex;align-items:center;gap:14px}
  .wordmark__dot{width:14px;height:14px;border-radius:50%;background:var(--navy)}
  .wordmark__name{
    font-family:"Cinzel",Georgia,serif;
    font-weight:500;
    color:var(--navy);
    letter-spacing:.02em;
    line-height:1;
  }
  .card--front .wordmark{position:absolute;left:50%;top:50%;transform:translate(-50%,-50%)}
  .card--front .wordmark__name{font-size:40px}
  .card--front .wordmark__dot{width:22px;height:22px}

  .card--back .wordmark{position:absolute;left:40px;top:44px}
  .card--back .wordmark__name{font-size:30px}

  .address{
    position:absolute;right:40px;top:40px;
    font-size:14px;line-height:1.45;color:var(--slate);
  }
  .address__crn{font-size:12px}

  .person{position:absolute;left:40px;top:158px;display:flex;align-items:baseline;gap:14px}
  .person__name{font-size:22px;color:var(--slate)}
  .person__role{font-family:"Cinzel",Georgia,serif;font-size:11px;letter-spacing:.06em;color:var(--slate)}

  .rule{
    position:absolute;left:40px;right:40px;top:204px;height:2px;
    background:linear-gradient(90deg,var(--navy),var(--blue) 60%,var(--navy));
  }

  .contacts{position:absolute;left:40px;top:222px;list-style:none;font-size:15px;line-height:1.7}
  .contacts li{display:flex;align-items:center;gap:12px}
  .contacts svg{width:13px;height:13px;flex:none}
</style>
</head>
<body>
  <section class="card card--front" aria-label="Card front">
    <div class="wordmark">
      <span class="wordmark__dot"></span>
      <span class="wordmark__name">Tarlow Financial</span>
    </div>
  </section>

  <section class="card card--back" aria-label="Card back">
    <div class="wordmark">
      <span class="wordmark__dot"></span>
      <span class="wordmark__name">Tarlow Financial</span>
    </div>

    <address class="address" style="font-style:normal">
      PO Box 527<br>
      Larkfield, Victoria, 3188<br>
      <span class="address__crn">Credit Rep No. : 918354</span>
    </address>

    <div class="person">
      <span class="person__name">Renata Sollisford</span>
      <span class="person__role">MANAGING DIRECTOR</span>
    </div>

    <div class="rule"></div>

    <ul class="contacts">
      <li>
        <svg viewBox="0 0 12 12" aria-hidden="true"><rect x="2.5" y="0.5" width="7" height="11" rx="1.2" fill="var(--slate)"/><rect x="3.8" y="2" width="4.4" height="6.5" fill="var(--paper)"/></svg>
        0491 738 205
      </li>
      <li>
        <svg viewBox="0 0 12 12" aria-hidden="true"><circle cx="6" cy="6" r="6" fill="var(--slate)"/><rect x="2.8" y="3.8" width="6.4" height="4.4" fill="var(--paper)"/><path d="M2.8 3.8 6 6.4 9.2 3.8" stroke="var(--slate)" stroke-width=".8" fill="none"/></svg>
        r.sollisford@tarlowfinancial.example.au
      </li>
      <li>
        <svg viewBox="0 0 12 12" aria-hidden="true"><circle cx="6" cy="6" r="6" fill="var(--slate)"/><circle cx="6" cy="6" r="3.6" fill="none" stroke="var(--paper)" stroke-width=".8"/><path d="M2.4 6h7.2M6 2.4c-1.6 2-1.6 5.2 0 7.2M6 2.4c1.6 2 1.6 5.2 0 7.2" stroke="var(--paper)" stroke-width=".7" fill="none"/></svg>
        www.tarlowfinancial.example.au
      </li>
    </ul>
  </section>
</body>
</html>
```